Vantrel Consulting Business card design.

See our website www.vantrelconsulting.com which will give you a good idea of what we are about. The font is called 'Play'.

I'd like a standout business card in keeping with the themes and branding on the website

Target Market(s)

professionals. HR directors

Industry/Entity Type

Business

Contact Information for Business Card

Vantrel Consulting PO Box 3917 Marrowdene NSW 2279 1300 584 316 Gareth Lindqvane Principal email: career@vantrelconsulting.com ABN: 41293087614

Other font styles liked:
• Play

Requirements
Must have
• Must have same design colours and branding as website.
• On back I'd prefer a list of the things we do which appears below the name at the header on the website

```html
<!DOCTYPE html>
<html lang="en">
<head>
<meta charset="utf-8">
<title>Vantrel Consulting — Business Card</title>
<link href="https://fonts.googleapis.com/css2?family=Play:wght@400;700&display=swap" rel="stylesheet">
<style>
  :root {
    --backdrop: #a8a5a5;
    --navy: #12283c;
    --accent: #2b93dc;
    --band: #2a9be6;
    --white: #ffffff;
  }
  * { margin: 0; padding: 0; box-sizing: border-box; }
  html, body {
    width: 1200px; height: 1200px; overflow: hidden;
    background: var(--backdrop);
    font-family: "Play", sans-serif;
  }
  .canvas { position: relative; width: 1200px; height: 1200px; }
  .card {
    position: absolute; width: 713px; height: 420px;
    background: var(--navy); overflow: hidden;
  }
  .card--front { left: 238px; top: 117px; }
  .card--back { left: 231px; top: 643px; }

  /* front */
  .front-wordmark {
    position: absolute; left: 0; right: 0; top: 122px;
    text-align: center; color: var(--white);
    font-size: 58px; font-weight: 400; letter-spacing: 1px; line-height: 1;
  }
  .front-services {
    position: absolute; left: 0; right: 0; top: 190px;
    text-align: center; color: var(--accent);
    font-size: 16px; letter-spacing: 2px;
  }
  .front-web {
    position: absolute; left: 0; right: 0; top: 347px;
    display: flex; justify-content: center; align-items: center; gap: 12px;
    color: var(--white); font-size: 18px;
  }
  .front-web .domain { color: var(--accent); }
  .front-web .rule { width: 34px; height: 2px; background: var(--accent); }

  /* back */
  .back-wordmark {
    position: absolute; left: 46px; top: 136px; width: 256px;
    text-align: center; color: var(--white); line-height: 1;
  }
  .back-wordmark .line-1 { display: block; font-size: 61px; letter-spacing: 1px; }
  .back-wordmark .line-2 { display: block; font-size: 42px; margin-top: 4px; letter-spacing: 1px; }

  .contact { position: absolute; left: 364px; top: 90px; color: var(--white); }
  .contact .name { color: var(--accent); font-size: 21px; font-weight: 700; }
  .contact .role { font-size: 15px; margin-top: 8px; }
  .contact ul { list-style: none; margin-top: 18px; }
  .contact li { display: flex; align-items: center; font-size: 16px; height: 24px; }
  .contact li svg { width: 16px; height: 14px; margin-right: 16px; fill: var(--accent); }
  .contact .abn { font-size: 16px; margin-top: 6px; }
  .contact .abn .label { color: var(--accent); }
  .contact .address { font-size: 16px; margin-top: 7px; }

  .service-band {
    position: absolute; left: 0; right: 0; bottom: 0; height: 50px;
    background: var(--band); color: var(--white);
    display: flex; align-items: center; justify-content: center;
    font-size: 18px; letter-spacing: 1px;
  }
</style>
</head>
<body>
<main class="canvas">

  <section class="card card--front" aria-label="Card front">
    <div class="front-wordmark">VANTREL CONSULTING</div>
    <div class="front-services">Search &amp; Select | Career | Coaching | Leadership | Outplacement</div>
    <div class="front-web">
      <span class="rule"></span>
      <span>www.<span class="domain">vantrelconsulting</span>.com</span>
      <span class="rule"></span>
    </div>
  </section>

  <section class="card card--back" aria-label="Card back">
    <div class="back-wordmark">
      <span class="line-1">VANTREL</span>
      <span class="line-2">CONSULTING</span>
    </div>

    <div class="contact">
      <div class="name">Gareth Lindqvane</div>
      <div class="role">Principal</div>
      <ul>
        <li>
          <svg viewBox="0 0 16 14" aria-hidden="true"><path d="M1 4c0-2 2-3 7-3s7 1 7 3v1h-4V3.5H5V5H1z"/><path d="M3 6h10l1 7H2z"/></svg>
          1300 584 316
        </li>
        <li>
          <svg viewBox="0 0 16 14" aria-hidden="true"><circle cx="8" cy="7" r="6.5"/><path d="M1.5 7h13M8 .5v13M3 3.5h10M3 10.5h10" stroke="#12283c" stroke-width="1" fill="none"/></svg>
          www.vantrelconsulting.com
        </li>
        <li>
          <svg viewBox="0 0 16 14" aria-hidden="true"><rect x="1" y="2" width="14" height="10"/><path d="M1 2l7 6 7-6M1 12l5-5M15 12l-5-5" stroke="#12283c" stroke-width="1.2" fill="none"/></svg>
          career@vantrelconsulting.com
        </li>
      </ul>
      <div class="abn"><span class="label">ABN:</span> 41293087614</div>
      <div class="address">PO Box 3917 Marrowdene NSW 2279</div>
    </div>

    <div class="service-band">Search &amp; Select | Career | Coaching | Leadership | Outplacement</div>
  </section>

</main>
</body>
</html>
```